Retail korea clothing store needs a logo desgin

Retail clothing store. Our main customer is 28-35 years women. our store is located at japan town San Francisco. our theme color are black , White and sliver color. we would like modern.

Clothing

```html
<!DOCTYPE html>
<html lang="en">
<head>
<meta charset="utf-8">
<title>Vemi – Business Cards</title>
<link href="https://fonts.googleapis.com/css2?family=Open+Sans:wght@400;600;800&display=swap" rel="stylesheet">
<style>
  :root {
    --backdrop: #aabfc1;
    --ink: #000000;
    --paper: #ffffff;
    --petal-dark: #111111;
    --petal-light: #f4f4f4;
  }
  * { box-sizing: border-box; margin: 0; padding: 0; }
  html, body {
    width: 1114px;
    height: 1200px;
    overflow: hidden;
    background: var(--backdrop);
    font-family: "Open Sans", Arial, sans-serif;
  }
  .canvas { position: relative; width: 1114px; height: 1200px; }

  .card {
    position: absolute;
    width: 524px;
    height: 288px;
    border-radius: 30px;
    overflow: hidden;
  }
  .card--front { left: 294px; top: 247px; background: var(--paper); }
  .card--back  { left: 282px; top: 580px; background: var(--ink); }

  .flower {
    position: absolute;
    width: 220px;
    height: 220px;
    border-radius: 50%;
  }
  .card--front .flower {
    left: 310px; top: -6px;
    background: radial-gradient(circle, var(--paper) 0 14%, var(--petal-dark) 15% 100%);
  }
  .card--back .flower {
    left: 309px; top: -3px;
    background: radial-gradient(circle, var(--ink) 0 14%, var(--petal-light) 15% 100%);
  }

  .contact-list {
    position: absolute;
    left: 46px;
    top: 44px;
    list-style: none;
  }
  .contact-item {
    display: flex;
    align-items: center;
    height: 28px;
    margin-bottom: 13px;
    color: var(--ink);
    font-size: 17px;
    font-weight: 400;
    letter-spacing: 0.2px;
    white-space: nowrap;
  }
  .contact-item--small { font-size: 13.5px; }
  .contact-icon {
    width: 28px;
    height: 28px;
    margin-right: 6px;
    flex: none;
  }

  .brand-name {
    position: absolute;
    left: 46px;
    top: 78px;
    color: var(--paper);
    font-size: 96px;
    font-weight: 800;
    line-height: 1;
    letter-spacing: -1px;
  }
</style>
</head>
<body>
<main class="canvas">

  <section class="card card--front" aria-label="Business card front">
    <ul class="contact-list">
      <li class="contact-item">
        <svg class="contact-icon" viewBox="0 0 28 28" aria-hidden="true">
          <circle cx="14" cy="14" r="13" fill="var(--ink)"/>
          <rect x="7" y="9" width="14" height="10" rx="1.5" fill="none" stroke="var(--paper)" stroke-width="1.8"/>
          <path d="M7.5 10 L14 15 L20.5 10" fill="none" stroke="var(--paper)" stroke-width="1.8"/>
        </svg>
        HELLO@VEMI-STORE.COM
      </li>
      <li class="contact-item">
        <svg class="contact-icon" viewBox="0 0 28 28" aria-hidden="true">
          <circle cx="14" cy="14" r="12" fill="none" stroke="var(--ink)" stroke-width="2.2"/>
          <path d="M10 8 L12.5 8 L13.5 11 L12 12.5 Q13.5 15.5 15.5 16 L17 14.5 L20 15.5 L20 18 Q19 20 16.5 19.5 Q10 17.5 8.5 11.5 Q8.5 8.5 10 8 Z" fill="var(--ink)"/>
        </svg>
        +1 415 555 0142
      </li>
      <li class="contact-item contact-item--small">
        <svg class="contact-icon" viewBox="0 0 28 28" aria-hidden="true">
          <circle cx="14" cy="14" r="13" fill="var(--ink)"/>
          <path d="M7 14 L14 7.5 L21 14 M9.5 12.5 V20 H18.5 V12.5" fill="none" stroke="var(--paper)" stroke-width="1.8"/>
          <rect x="12.5" y="15.5" width="3" height="4.5" fill="var(--paper)"/>
        </svg>
        YOUR COMPANY ADDRESS
      </li>
      <li class="contact-item contact-item--small">
        <svg class="contact-icon" viewBox="0 0 28 28" aria-hidden="true">
          <circle cx="14" cy="14" r="13" fill="var(--ink)"/>
          <circle cx="14" cy="14" r="7" fill="none" stroke="var(--paper)" stroke-width="1.6"/>
          <ellipse cx="14" cy="14" rx="3" ry="7" fill="none" stroke="var(--paper)" stroke-width="1.4"/>
          <path d="M7 14 H21" stroke="var(--paper)" stroke-width="1.4"/>
        </svg>
        WWW.VEMI-STORE.COM
      </li>
    </ul>
    <div class="flower" role="img" aria-label="Black stylised flower bloom ornament"></div>
  </section>

  <section class="card card--back" aria-label="Business card back">
    <p class="brand-name">Vemi</p>
    <div class="flower" role="img" aria-label="White stylised flower bloom ornament"></div>
  </section>

</main>
</body>
</html>
```